Kivo Commercial Cleaning is lookong for a new business card design.

A fresh new design that's professional and stylish. We need a serious upgrade to our business cards. I have included pictures of our existing ones. Our clients include professional individuals and business owners. We woupdblike something professional and upbeat. Please have fun and see what you come uo with.

Target Market(s)

Property managers, business owners, facility managers and other similar professionals

Industry/Entity Type

Janitorial

Contact Information for Business Card

Name, cell, office number, email, web address

Font styles to use
Sans Serif

Colors

Designer to choose colors to be used in the design.

Requirements
Must have
• please use the green color in our logo
Nice to have
• Bar code
Should not have
• Address

```html
<!DOCTYPE html>
<html lang="en">
<head>
<meta charset="utf-8">
<title>Kivo Commercial Cleaning – Business Card</title>
<link rel="stylesheet" href="https://fonts.googleapis.com/css2?family=Open+Sans:wght@400;600;700;800&display=swap">
<style>
  :root {
    --page: #e8e4de;
    --card-dark: #222226;
    --card-edge: #18181b;
    --brand-green: #3ab54a;
    --brand-blue: #3e72ad;
    --deep-blue: #0a5796;
    --text-light: #f2f2f2;
    --ghost: #161618;
  }
  * { box-sizing: border-box; margin: 0; padding: 0; }
  html, body { width: 1200px; height: 780px; overflow: hidden; }
  body {
    background: var(--page);
    font-family: "Open Sans", Arial, sans-serif;
    display: flex;
    align-items: center;
    justify-content: center;
    gap: 56px;
  }
  .card {
    position: relative;
    width: 525px;
    height: 300px;
    border-radius: 22px;
    background: var(--card-dark);
    overflow: hidden;
    box-shadow: 0 3px 0 var(--card-edge), 0 14px 28px rgba(0,0,0,.25);
  }

  /* Front */
  .front .brand-name {
    position: absolute;
    top: 24px; left: 118px;
    font-size: 64px;
    font-weight: 800;
    line-height: 1;
    color: var(--brand-green);
    letter-spacing: -1px;
  }
  .front .tagline {
    position: absolute;
    top: 96px; left: 96px;
    font-size: 15px;
    font-weight: 600;
    color: var(--brand-blue);
    letter-spacing: .3px;
  }
  .front .person {
    position: absolute;
    top: 130px; left: 0;
    display: flex;
    align-items: center;
    gap: 10px;
  }
  .front .person-bar {
    width: 12px; height: 26px;
    background: var(--brand-green);
  }
  .front .person-name {
    font-size: 27px;
    font-weight: 700;
    color: var(--brand-blue);
  }
  .front .person-name .first { color: var(--brand-green); }
  .front .contact-list {
    position: absolute;
    top: 178px; left: 22px;
    list-style: none;
  }
  .front .contact-list li {
    display: flex;
    align-items: center;
    gap: 8px;
    font-size: 13.5px;
    color: var(--text-light);
    line-height: 22px;
  }
  .front .contact-list svg { width: 12px; height: 12px; fill: var(--brand-green); flex: none; }
  .front .ghost-name {
    position: absolute;
    right: -6px; bottom: -30px;
    font-size: 150px;
    font-weight: 800;
    line-height: 1;
    color: var(--ghost);
    letter-spacing: -4px;
  }

  /* Back */
  .back .band {
    position: absolute;
    left: 0; right: 0;
    top: 40px; bottom: 40px;
    background: var(--brand-blue);
    display: flex;
    align-items: center;
    justify-content: center;
  }
  .back .brand-name {
    font-size: 150px;
    font-weight: 800;
    line-height: 1;
    color: var(--deep-blue);
    letter-spacing: -4px;
  }
</style>
</head>
<body>
  <section class="card front" aria-label="Business card front">
    <div class="ghost-name" aria-hidden="true">Kivo</div>
    <div class="brand-name">Kivo</div>
    <div class="tagline">commercial cleaning</div>
    <div class="person">
      <span class="person-bar"></span>
      <span class="person-name"><span class="first">Marco</span> Delgado</span>
    </div>
    <ul class="contact-list">
      <li>
        <svg viewBox="0 0 24 24" aria-hidden="true"><path d="M6.6 10.8a15.1 15.1 0 0 0 6.6 6.6l2.2-2.2a1 1 0 0 1 1-.25 11.4 11.4 0 0 0 3.6.57 1 1 0 0 1 1 1V20a1 1 0 0 1-1 1A17 17 0 0 1 3 4a1 1 0 0 1 1-1h3.5a1 1 0 0 1 1 1c0 1.25.2 2.45.57 3.57a1 1 0 0 1-.25 1z"/></svg>
        (512) 555-0187
      </li>
      <li>
        <svg viewBox="0 0 24 24" aria-hidden="true"><path d="M3 5h18v14H3zm2 2v.5l7 4.5 7-4.5V7z"/></svg>
        marco@kivocleaning.com
      </li>
      <li>
        <svg viewBox="0 0 24 24" aria-hidden="true"><circle cx="12" cy="12" r="10"/></svg>
        www.kivocleaning.com
      </li>
    </ul>
  </section>

  <section class="card back" aria-label="Business card back">
    <div class="band">
      <div class="brand-name">Kivo</div>
    </div>
  </section>
</body>
</html>
```